Business Cards for new orthopaedic surgery practice

My husband and I are starting our own orthopaedic surgery practice. We are looking for a business card that is uniform, but one will have my name/title and the other will have his. You can just create one design with my name on it for now. But when I choose your design as the winning design I will ask that you add another copy with his name/title.

We are looking for classy, simple, elite all in one. We like dark blues/a little gold/yellow. Something that goes with our logo. We want our logo incorporated. Here is all the info you need:
Business name: RV Spine & Vitality Center
Location: 38915 North Bramble Ave
Palm Hollow, FL 33480
Phone: 954-218-4630
Fax: 954-571-2846
Email: info@myrvspine.example

Names: Lucinda Ferrow, M.D.
Board Certified Hand and Upper Extremity Surgeon

Emeka Dlunga, M.D.
Board Certified Hip & Knee Replacement/General Orthopaedic Surgeon

Can decide what you want to put on the back. Maybe a slogan:
Grounded in Care. Centered on You

I am just going to upload our logo. The only thing is if we select you as the winning design, the location, and phone numbers may change. We will need your help to update that once fully solidified.

Industry/Entity Type

Medical

Contact Information for Business Card

Colors
0054AA
0677BA
7BADD7
CADEEF
E8F1F8
0094D4
00A9DD
6FCCEA
C7EBF8
E9F6FB

Requirements
Must have
• class, appeal,
Should not have
• We want to air on the side of masculine if we are looking at masculine vs. feminine feel. But we still want it classy, sophisticated, and something we will love

```html
<!DOCTYPE html>
<html lang="en">
<head>
<meta charset="utf-8">
<title>RV Spine &amp; Vitality Center — Business Card</title>
<link rel="stylesheet" href="https://fonts.googleapis.com/css2?family=Tinos:wght@400&display=swap">
<style>
  :root {
    --navy: #0f1f45;
    --navy-soft: #1a2d5a;
    --gold: #c9a04a;
    --ink: #3a3d44;
    --paper: #f4f4f5;
    --stage: #e6e3de;
    --white: #ffffff;
  }
  * { box-sizing: border-box; margin: 0; padding: 0; }
  html, body { width: 1200px; height: 900px; overflow: hidden; }
  body {
    background: var(--stage);
    font-family: "Tinos", "Times New Roman", serif;
    position: relative;
  }
  .card {
    position: absolute;
    left: 290px;
    width: 620px;
    height: 354px;
    border-radius: 30px;
    overflow: hidden;
    box-shadow: 0 10px 30px rgba(0,0,0,.18);
  }
  .card-texture {
    position: absolute;
    inset: 0;
  }

  /* Back side */
  .card-back {
    top: 66px;
    background: var(--navy);
    color: var(--white);
  }
  .card-back .card-texture {
    background: radial-gradient(ellipse at 55% 45%, var(--navy-soft), var(--navy) 70%);
  }
  .back-brand {
    position: absolute;
    top: 118px; left: 0; right: 0;
    text-align: center;
    font-size: 32px;
    font-weight: 400;
    color: var(--white);
  }
  .back-rule {
    position: absolute;
    height: 1px;
    background: var(--gold);
    opacity: .8;
  }
  .back-rule.upper { top: 168px; left: 300px; width: 250px; }
  .back-rule.lower { top: 214px; left: 70px; width: 250px; }
  .slogan {
    position: absolute;
    top: 181px; left: 0; right: 0;
    text-align: center;
    font-size: 16px;
    letter-spacing: 1.5px;
    text-transform: uppercase;
  }

  /* Front side */
  .card-front {
    top: 480px;
    background: var(--paper);
  }
  .card-front .card-texture {
    background: linear-gradient(160deg, var(--white), var(--paper) 55%, #e4e4e6);
  }
  .front-brand {
    position: absolute;
    left: 38px; top: 110px;
    width: 190px;
    display: flex;
    align-items: center;
    gap: 10px;
  }
  .brand-dot {
    width: 22px; height: 22px;
    border-radius: 50%;
    background: var(--navy);
    flex: none;
  }
  .brand-name {
    font-size: 22px;
    line-height: 1.2;
    color: var(--navy);
  }
  .details {
    position: absolute;
    right: 40px; top: 62px;
    text-align: right;
  }
  .person-name { font-size: 26px; font-weight: 400; color: var(--navy); }
  .person-title { font-size: 14.5px; color: var(--ink); margin-top: 4px; }
  .contact-list { list-style: none; margin-top: 16px; }
  .contact-list li {
    display: flex; justify-content: flex-end; align-items: center;
    gap: 10px;
    font-size: 16px; color: var(--ink);
    line-height: 27px;
  }
  .contact-list svg { width: 16px; height: 16px; fill: var(--gold); flex: none; }
  .front-rule {
    position: absolute;
    left: 250px; right: 40px; top: 262px;
    height: 1px; background: var(--navy); opacity: .6;
  }
  .address {
    position: absolute;
    right: 40px; top: 272px;
    display: flex; align-items: center; gap: 10px;
    font-size: 16px; color: var(--ink);
  }
  .address svg { width: 16px; height: 16px; fill: var(--gold); flex: none; }
</style>
</head>
<body>

<section class="card card-back" aria-label="Card back">
  <div class="card-texture" role="img" aria-label="Faint large tree silhouette in navy tones"></div>
  <div class="back-brand">RV Spine &amp; Vitality Center</div>
  <div class="back-rule upper"></div>
  <p class="slogan">Grounded in Care. Centered on You</p>
  <div class="back-rule lower"></div>
</section>

<section class="card card-front" aria-label="Card front">
  <div class="card-texture" role="img" aria-label="Faint large tree silhouette in light grey tones"></div>
  <div class="front-brand">
    <span class="brand-dot"></span>
    <span class="brand-name">RV Spine &amp; Vitality Center</span>
  </div>

  <div class="details">
    <h1 class="person-name">Lucinda Ferrow, M.D.</h1>
    <p class="person-title">Board Certified Hand and Upper Extremity Surgeon</p>
    <ul class="contact-list">
      <li>954-218-4630
        <svg viewBox="0 0 24 24" aria-hidden="true"><path d="M6.6 10.8a15 15 0 0 0 6.6 6.6l2.2-2.2a1 1 0 0 1 1-.25 11.4 11.4 0 0 0 3.6.57 1 1 0 0 1 1 1V20a1 1 0 0 1-1 1A17 17 0 0 1 3 4a1 1 0 0 1 1-1h3.5a1 1 0 0 1 1 1c0 1.25.2 2.45.57 3.57a1 1 0 0 1-.25 1z"/></svg>
      </li>
      <li>954-571-2846
        <svg viewBox="0 0 24 24" aria-hidden="true"><path d="M6 2h12v5H6zM4 8h16a2 2 0 0 1 2 2v6h-4v6H6v-6H2v-6a2 2 0 0 1 2-2zm4 8v4h8v-4z"/></svg>
      </li>
      <li>info@myrvspine.example
        <svg viewBox="0 0 24 24" aria-hidden="true"><path d="M2 5h20v14H2zm2 2v.5l8 5 8-5V7z"/></svg>
      </li>
    </ul>
  </div>

  <div class="front-rule"></div>
  <p class="address">38915 North Bramble Ave, Palm Hollow, FL 33480
    <svg viewBox="0 0 24 24" aria-hidden="true"><path d="M12 2a7 7 0 0 0-7 7c0 5 7 13 7 13s7-8 7-13a7 7 0 0 0-7-7zm0 9.5A2.5 2.5 0 1 1 12 6.5a2.5 2.5 0 0 1 0 5z"/></svg>
  </p>
</section>

</body>
</html>
```